Brochure Design Project

We are a consulting engineering company and need to have our current company brochure updated and made to look a lot more professional.

We provide design and documentation of electrical, lighting, mechanical, hydraulic, fire, services to architects, interior designers, building owners and managers.

We are launching an updated website shortly and want a print brochure to send to clients.

Attached is our current brochure for reference.
Updates

The recent projects section should be renamed to "Completed Projects". Space should be allowed for 8 projects. I have uploaded 7 of these images and a new image will follow shortly.

We would like to include an image for each of our company services. I have uploaded 9 new images:

1. Electrical
2. Mechanical
3. Communications
4. Fire
5. Security
6. Lighting
7. Hydraulics
8. Computer Suite
9. Building Assessments

Target Market(s)

Architects, Interior Designers, Consultants, Professionals

Industry/Entity Type

Building

Requirements
Must have
• Very professional look
Simple and easy to read layout
Similar look and feel to our new website which is soon to be launched : http://www.sitehaven.co.uk/rkm/
Examples of our recent projects - around 6 projects with 1 or 2 photos per project. Will upload these soon.
A3 size, double sided with centre fold
Should not have
• Bright colours
Any comics or similar

```html
<!DOCTYPE html>
<html lang="en">
<head>
<meta charset="utf-8">
<title>RKM Consulting Services – Brochure</title>
<link href="https://fonts.googleapis.com/css2?family=Open+Sans:wght@300;400;600;700&display=swap" rel="stylesheet">
<style>
:root{
  --ink:#2f3133;
  --muted:#4a4c4e;
  --dark:#1f1f1f;
  --band:#b8babb;
  --paper-top:#dfe0e1;
  --paper-bottom:#f3f3f3;
  --tick:#7fb23a;
  --arrow:#e0782a;
  --rule:#c9cacb;
}
*{margin:0;padding:0;box-sizing:border-box}
html,body{width:829px;height:1200px;overflow:hidden;background:#fff}
body{font-family:"Open Sans",Arial,sans-serif;color:var(--ink);position:relative}
.spread{position:absolute;left:0;width:829px}
.spread--outside{top:0;height:585px}
.spread--inside{top:592px;height:608px}
.band-top{position:absolute;left:0;right:0;top:0;background:var(--band)}
.band-rule{position:absolute;left:0;right:0;background:var(--dark)}
.paper{position:absolute;left:0;right:0;background:linear-gradient(180deg,var(--paper-top),var(--paper-bottom) 55%,var(--paper-top))}
.footer{position:absolute;left:0;right:0;bottom:0;background:var(--dark)}
.fold{position:absolute;left:414px;top:0;bottom:0;width:1px;background:rgba(255,255,255,.35)}
.bar{position:absolute;background:var(--dark)}
.foot-mark{position:absolute;font-weight:300;font-size:25px;color:#8d8f91;letter-spacing:-.5px}
.block{position:absolute;font-size:6.9px;line-height:9.3px;color:var(--muted)}
.block p{margin-bottom:4.5px}
.heading{font-size:8.6px;font-weight:700;color:var(--ink);letter-spacing:.3px;margin-bottom:9px}
.ticks,.arrows{list-style:none}
.ticks li,.arrows li{position:relative;padding-left:12px}
.ticks li::before{content:"";position:absolute;left:2px;top:1px;width:3px;height:6px;border-right:2px solid var(--tick);border-bottom:2px solid var(--tick);transform:rotate(40deg)}
.arrows li::before{content:"";position:absolute;left:1px;top:3px;width:6px;height:2px;background:var(--arrow);transform:rotate(35deg)}
.rule{position:absolute;height:1px;background:var(--rule)}
.photo{position:absolute;border:1px solid #fff;box-shadow:0 2px 4px rgba(0,0,0,.35);border-radius:2px}
.logo{position:absolute;left:467px;top:44px}
.logo .name{font-weight:400;font-size:44px;line-height:46px;color:var(--dark);letter-spacing:1px}
.logo .sub{font-size:5px;font-weight:600;letter-spacing:.9px;color:var(--dark)}
.quote{position:absolute;text-align:center;color:var(--ink)}
.quote--feature{left:491px;width:270px;top:404px;font-size:13.4px;line-height:17.6px;font-weight:300}
.quote--feature b{font-weight:700;font-size:16.5px}
.quote--wide{left:240px;width:346px;top:845px;font-size:15.2px;line-height:20.3px;font-weight:400}
.list{font-size:6.7px;line-height:9.1px}
</style>
</head>
<body>

<section class="spread spread--outside">
  <div class="band-top" style="height:22px"></div>
  <div class="band-rule" style="top:22px;height:11px"></div>
  <div class="paper" style="top:33px;height:484px"></div>
  <div class="footer" style="height:68px"></div>
  <div class="fold"></div>

  <div class="bar" style="left:33px;top:33px;width:9px;height:238px"></div>
  <div class="bar" style="left:370px;top:277px;width:10px;height:240px"></div>
  <div class="bar" style="left:447px;top:33px;width:10px;height:230px"></div>
  <div class="bar" style="left:787px;top:277px;width:10px;height:240px"></div>

  <div class="block" style="left:59px;top:46px;width:292px">
    <h2 class="heading">ABOUT US</h2>
    <p>RKM was formed in November 1998 and has evolved into one of Perth's leading building services consulting practices.</p>
    <p>Our award winning projects cover all states and territories of Australia demonstrating our depth of experience.</p>
    <p>We work with all sectors of the property, infrastructure, mining, oil and gas and construction industries delivering, complex, multidiscipline building services engineering solutions.</p>
    <p>Our client base includes national, state and local governments, developers, tenants, builders, architects, project managers, interior designers and property/portfolio managers.</p>
    <p>RKM provides design, documentation and contract administration services associated with:</p>
    <ul class="ticks">
      <li>Mechanical</li><li>Communications</li><li>Fire</li><li>Security</li>
      <li>Lighting</li><li>Hydraulics</li><li>Computer Suite</li><li>Building Assessments</li>
    </ul>
  </div>
  <div class="photo" role="img" aria-label="Boardroom with long table, black chairs and brick wall" style="left:203px;top:203px;width:147px;height:98px;background:linear-gradient(135deg,#d8d6d2,#9b8a7c 55%,#5a4d45)"></div>

  <div class="block" style="left:59px;top:297px;width:300px">
    <h2 class="heading" style="margin-bottom:6px">OBJECTIVES</h2>
    <p>To provide the optimum,cost effective, energy<br>efficient design solutions using the latest technological innovations.</p>
    <p>Our team at RKM aspires to:-</p>
    <ul class="arrows">
      <li>Surpass client expectation</li>
      <li>Ensure client understanding of design concepts</li>
      <li>Ensure timely provision of design input allowing ample time for consideration and inclusion</li>
    </ul>
  </div>
  <div class="rule" style="left:240px;top:403px;width:140px"></div>

  <div class="block" style="left:59px;top:409px;width:305px">
    <h2 class="heading" style="margin-bottom:8px">WORK ETHIC</h2>
    <p style="margin-bottom:0">To protect the engineering interests of our clients from initial involvement to the conclusion of each project<br>To provide:-</p>
    <ul class="ticks">
      <li>A level of diligence, based on sound preparation that will ensure client satisfaction</li>
      <li>Innovation in design</li>
      <li>A service orientated and responsive approach</li>
      <li>Continual implementation across all aspects of each project</li>
      <li>A unique, detailed and focused approach to each project</li>
    </ul>
  </div>

  <div class="logo">
    <div class="name">RKM</div>
    <div class="sub">Consulting Services Pty Ltd</div>
  </div>
  <div class="photo" role="img" aria-label="Lime green upholstered meeting booth with table and phone" style="left:491px;top:115px;width:266px;height:266px;background:linear-gradient(180deg,#8fa21a,#b9cc2c 40%,#a5bb1f 70%,#7f9112)"></div>

  <div class="quote quote--feature">“<b>Every project</b> receives a level of <b>dedication,<br>commitment</b> and service<br>to ensure<br>client <b>expectations</b> are<br><b>exceeded</b>”</div>

  <div class="foot-mark" style="left:22px;top:528px">rkm</div>
  <div class="foot-mark" style="left:758px;top:528px">rkm</div>
</section>

<section class="spread spread--inside">
  <div class="band-top" style="height:44px"></div>
  <div class="band-rule" style="top:44px;height:12px"></div>
  <div class="paper" style="top:56px;height:483px"></div>
  <div class="footer" style="height:69px"></div>
  <div class="fold"></div>

  <div class="bar" style="left:32px;top:56px;width:9px;height:238px"></div>
  <div class="bar" style="left:787px;top:298px;width:10px;height:241px"></div>

  <div class="block list" style="left:58px;top:65px;width:240px">
    Electrical Services<br>Feature lighting for highlight/contrast of client orientated areas<br>Power distribution<br>General lighting<br>Programmable lighting control<br>Emergency lighting and exit signs<br>Electrical consumption management<br>Lighting control integration with energy<br>management systems<br>Evacuation warning systems<br>Power conditioners<br>Public address installations<br>Television signal distribution
  </div>
  <div class="block list" style="left:58px;top:195px;width:150px">
    Hydraulic Services<br>Water supplies<br>Waste discharge<br>Venting<br>Water heating and cooling<br>Filtration
  </div>
  <div class="block list" style="left:58px;top:387px;width:190px">
    Critical Use Installations<br>Layout and space allowance for hardware and equipment<br>Uninterruptable power supplies and power conditioning<br>Access control and intruder detection<br>Fire rating<br>Anti static solutions<br>PABX and VOIP integration<br>Dedicated electrical distribution systems<br>Stand-by power supplies<br>High heat rejection cooling solutions
  </div>
  <div class="block list" style="left:58px;top:490px;width:190px">
    Computer Suite Audits<br>Comprehensive Computer Suite Audits<br>Australian Standard Compliance<br>TIA 942 Tier Rating certification
  </div>
  <div class="block list" style="left:619px;top:68px;width:135px">
    Communication Systems<br>Telephone cabling<br>Data cabling<br>Patching philosophies<br>Fibre optic distribution systems<br>Integration of voice and<br>data cabling systems<br>Hardware housings<br>Compliance with relevant codes and installation practices<br>LAN Cable distribution systems
  </div>
  <div class="block list" style="left:619px;top:200px;width:150px">
    Fire Services<br>Electronic Smoke and Thermal Detection<br>ASD Systems<br>Fire Suppression Systems<br>Fire Sprinkler Systems
  </div>
  <div class="block list" style="left:619px;top:396px;width:140px">
    Mechanical Services<br>District Cooling System<br>Air and Water Cooled Chilled Water<br>System<br>BMS/BAS and DDC Control System<br>Computer and Data Centre Solutions<br>DX-Type Water and Air<br>Cooled System (Single or<br>Multiple Indoor Units)<br>VAV and Chilled Beams<br>Industrial and Commercial<br>Humidification<br>Commercial and Industrial Evaporative<br>Cooling Using Air Washers
  </div>
  <div class="block list" style="left:249px;top:471px;width:150px">
    Security Services<br>Electronic access control<br>Integration of existing systems with<br>client requirements<br>Intruder detection<br>Off site monitoring and alarms
  </div>
  <div class="block list" style="left:430px;top:471px;width:160px">
    Building Assessment<br>Building services condition assessment<br>Advise relative to available building services<br>Trouble Shooting and Investigation<br>Review of Existing Systems<br>Upgrade for Current and Future Refurbishment
  </div>

  <div class="photo" role="img" aria-label="Boardroom with long table and brick wall" style="left:249px;top:117px;width:147px;height:97px;background:linear-gradient(135deg,#d8d6d2,#9b8a7c 55%,#5a4d45)"></div>
  <div class="photo" role="img" aria-label="Large open hall with ceiling lights" style="left:430px;top:117px;width:147px;height:97px;background:linear-gradient(180deg,#3a342f,#8b7c6e 45%,#c9c0b4)"></div>
  <div class="photo" role="img" aria-label="Meeting room with projector screen and chairs" style="left:58px;top:260px;width:147px;height:96px;background:linear-gradient(180deg,#e9e7e2,#b8b4ac 55%,#3b3d44)"></div>
  <div class="photo" role="img" aria-label="Illuminated two-storey building at dusk" style="left:620px;top:260px;width:147px;height:96px;background:linear-gradient(180deg,#1e2a4a,#3d4a6e 40%,#c98a3c 65%,#4a5a2a)"></div>
  <div class="photo" role="img" aria-label="Open plan office with workstations" style="left:249px;top:363px;width:147px;height:97px;background:linear-gradient(180deg,#e6e6e4,#b9bcbd 50%,#3d3f42)"></div>
  <div class="photo" role="img" aria-label="Reception area with dark ceiling and harbour view" style="left:430px;top:363px;width:147px;height:97px;background:linear-gradient(180deg,#1c1c1c,#6d6a66 45%,#b8b2aa)"></div>
  <div class="rule" style="left:430px;top:218px;width:147px"></div>

  <div class="quote quote--wide">“Every project receives a level of dedication, commitment and service to ensure client expectations are exceeded”</div>

  <div class="foot-mark" style="left:22px;top:1143px;position:fixed"></div>
  <div class="foot-mark" style="left:22px;top:551px">rkm</div>
  <div class="foot-mark" style="left:758px;top:551px">rkm</div>
</section>

</body>
</html>
```